Animal Facility Brochure for Pet Boarding, Boutique, Doggie Daycare, Grooming

This brochure is for a Doggie Daycare, Pet Grooming, Dog Boarding & Pet Boutique for the Hollowmere Pet Lodge & Spa.

Hi there! I am in need of a brochure done for my new up and coming business.
The business will involve Dog/Cat Grooming, Dog Boarding, Doggie Daycare, & a small pet boutique. I am looking for something that stands out and is modern and chic and follows the look of the pictures i have posted (Pim and Tessel) . My color scheme of my business is gray & white. Also i need the brochure to be easily able to understand what we are trying to get across and is easy to read. I am very proud of my logo that was created using craft hive and would love that incorporated. also i have attached the information that will need to be in the brochure for the client. I am looking for someone who can devote some time working with me on this because this is my first time. I am sure there will need to be some changes so i need someone who is patient. The picture of the projected look of my sign is gearing more towards something clean and modern.

Industry/Entity Type

Pet Care

Colors
f5f5f5
f8f8f8
dbdbdb
959595
aaaaaa
85abd2
cedeed
eaf1f7

Requirements
Nice to have
• File nine for Grooming, Boarding, Daycare, Pet Boutique

```html
<!DOCTYPE html>
<html lang="en">
<head>
<meta charset="utf-8">
<title>Hollowmere Pet Lodge &amp; Spa — Brochure</title>
<link href="https://fonts.googleapis.com/css2?family=Bangers&family=Crimson+Text:wght@400;600&display=swap" rel="stylesheet">
<style>
:root{
  --page:#ffffff;
  --paper:#f5f5f5;
  --paper-shade:#dbdbdb;
  --blue-deep:#2f5f99;
  --blue-mid:#4f80b8;
  --blue-soft:#85abd2;
  --blue-pale:#cedeed;
  --ink:#1b1b1b;
  --silhouette:#161616;
  --photo-warm:#b8a48e;
  --photo-cool:#9a9a9a;
  --table-line:#c0392b;
}
*{margin:0;padding:0;box-sizing:border-box}
html,body{width:1200px;height:1200px;overflow:hidden;background:var(--page)}
.canvas{position:relative;width:1200px;height:1200px;background:var(--page);font-family:"Crimson Text",serif;color:var(--ink)}
.sheet{position:absolute;overflow:hidden;background:linear-gradient(90deg,var(--paper) 0%,#fff 30%,var(--paper-shade) 33.3%,#fff 36%,#f8f8f8 64%,var(--paper-shade) 66.6%,#fff 69%,var(--paper) 100%)}
.sheet--outside{left:88px;top:422px;width:429px;height:396px}
.sheet--inside{left:550px;top:419px;width:432px;height:397px}
.facets{position:absolute;inset:0;width:100%;height:100%}
.panel{position:absolute;top:0;height:100%;text-align:center}
.heading{font-family:"Bangers",sans-serif;letter-spacing:.5px;color:var(--ink);font-weight:400}
.body{line-height:1.38}
.photo{position:absolute}
.silhouette{position:absolute;background:var(--silhouette);z-index:2}

/* outside sheet */
.mission{left:8px;width:126px;top:86px}
.mission .heading{font-size:9px}
.mission .body{font-size:5.6px;margin-top:2px}
.hours{left:148px;width:128px;top:86px}
.hours .heading{font-size:9px;margin-bottom:6px}
.hours li{list-style:none;font-size:7px;line-height:21.6px}
.hours .photo{left:32px;top:162px;width:47px;height:100px;background:linear-gradient(180deg,var(--photo-warm),var(--photo-cool))}
.cover{left:288px;width:141px;top:134px}
.brand{margin:0 auto;width:70px;height:84px;display:flex;flex-direction:column;align-items:center;justify-content:center;gap:4px}
.brand-mark{width:10px;height:10px;border-radius:50%;background:#6b3e2a}
.brand-name{font-size:8px;color:#6b3e2a;line-height:1.1}
.tagline{font-size:5.8px;margin-top:8px;padding:0 8px}
.address{font-size:5.6px;margin-top:10px}
.contact{position:absolute;left:0;top:198px;width:141px;font-size:5.4px;color:#fff;line-height:1.6}
.contact b{font-family:"Bangers",sans-serif;font-weight:400;letter-spacing:.3px}

/* inside sheet */
.about{left:8px;width:128px;top:74px}
.tiny{font-size:4.4px;line-height:1.35}
.about .heading,.rates .heading,.stay .heading{font-size:6px;margin:7px 0 3px}
.about .photo{left:24px;top:206px;width:60px;height:48px;background:linear-gradient(135deg,var(--photo-cool),var(--photo-warm))}
.rates{left:148px;width:134px;top:56px}
.rates .heading:first-child{margin-top:0}
.rate-table{margin:6px auto 0;border-collapse:collapse;width:66px;font-size:3.2px}
.rate-table td{border:.4px solid var(--table-line);height:8px;padding:0 1px;text-align:left}
.rates .photo{left:47px;top:227px;width:40px;height:62px;background:linear-gradient(180deg,#6b5a4a,var(--photo-warm))}
.stay{left:292px;width:136px;top:61px}
.stay p{margin-bottom:7px}
.stay .heading{margin:4px 0 2px;white-space:nowrap;font-size:5.4px}
.stay .photo{left:46px;top:207px;width:46px;height:65px;background:linear-gradient(180deg,#d8c2a6,#b89a78)}
</style>
</head>
<body>
<main class="canvas">

  <section class="sheet sheet--outside" aria-label="Brochure outside">
    <svg class="facets" viewBox="0 0 429 396" preserveAspectRatio="none" role="img" aria-label="Blue faceted geometric bands top and bottom">
      <defs>
        <linearGradient id="bandA" x1="0" y1="0" x2="1" y2="1"><stop offset="0" stop-color="#85abd2"/><stop offset=".5" stop-color="#4f80b8"/><stop offset="1" stop-color="#2f5f99"/></linearGradient>
        <linearGradient id="bandB" x1="0" y1="1" x2="1" y2="0"><stop offset="0" stop-color="#2f7fb5"/><stop offset=".5" stop-color="#4f80b8"/><stop offset="1" stop-color="#3b6aa6"/></linearGradient>
      </defs>
      <polygon fill="url(#bandA)" points="0,0 429,0 429,170 360,100 300,40 240,70 175,85 145,60 100,80 0,85"/>
      <polygon fill="url(#bandB)" points="0,396 429,396 429,240 360,285 300,320 240,300 175,300 140,280 70,290 0,325"/>
    </svg>

    <div class="panel mission">
      <h2 class="heading">Our Mission:</h2>
      <p class="body">is to care for your pet in the best way possible when you are away. We provide a unique social experience for dogs and create a new standard for dog care. Our Kitty condo provides a safe and quiet atmosphere for your kitty. We have set out to create a facility that exemplifies what we ourselves would want for our own best friends. Your pet will have a fun, safe place to play during the day and a secure night time environment when lodging with us. Our staff will go to any lengths to make our guest's stay a true delight. Our professional spa and grooming salon offers a wide range of services for your dog and cat. Our experienced groomers are friendly and knowledgeable and have the expertise to help your pet look and feel its best while exceeding your expectations.</p>
    </div>

    <div class="panel hours">
      <h2 class="heading">Hours of Operation</h2>
      <ul>
        <li>Monday 7:30am- 6:30pm</li>
        <li>Tuesday 7:30am- 6:30pm</li>
        <li>Wednesday 7:30am- 6:30pm</li>
        <li>Thursday 7:30am- 6:30pm</li>
        <li>Friday 7:30am- 6:30pm</li>
        <li>Saturday 8:30am- 6:30pm</li>
        <li>Sunday 10:30am- 6:30pm</li>
      </ul>
      <div class="photo" role="img" aria-label="Photo of the boutique shelves and spa interior"></div>
    </div>

    <div class="panel cover">
      <div class="brand">
        <span class="brand-mark"></span>
        <span class="brand-name">HOLLOWMERE PET<br>LODGE &amp; SPA</span>
      </div>
      <p class="tagline">When it comes to your pet, we will stop at nothing to keep them healthy, happy and well-loved</p>
      <p class="address">120 Elm Crest Road<br>Hollowmere, OH 44021</p>
      <p class="contact"><b>Website:</b> www.hollowmerepetlodge.com<br><b>Email:</b>info@hollowmerepetlodge.com</p>
    </div>
  </section>

  <section class="sheet sheet--inside" aria-label="Brochure inside">
    <svg class="facets" viewBox="0 0 432 397" preserveAspectRatio="none" role="img" aria-label="Blue faceted geometric bands top and bottom">
      <defs>
        <linearGradient id="bandC" x1="0" y1="0" x2="1" y2="1"><stop offset="0" stop-color="#2f6fb0"/><stop offset=".5" stop-color="#85abd2"/><stop offset="1" stop-color="#3b6aa6"/></linearGradient>
        <linearGradient id="bandD" x1="0" y1="0" x2="1" y2="0"><stop offset="0" stop-color="#2f7fb5"/><stop offset=".5" stop-color="#4f80b8"/><stop offset="1" stop-color="#2f5f99"/></linearGradient>
      </defs>
      <polygon fill="url(#bandC)" points="0,0 432,0 432,10 380,40 350,25 300,30 250,48 180,50 140,65 100,45 60,55 0,52"/>
      <polygon fill="url(#bandD)" points="0,397 432,397 432,345 400,330 350,345 290,325 220,340 180,320 140,330 80,330 0,335"/>
    </svg>

    <div class="silhouette" role="img" aria-label="Dog bone silhouette" style="left:64px;top:15px;width:52px;height:26px;border-radius:12px"></div>
    <div class="silhouette" role="img" aria-label="Paw print silhouette" style="left:402px;top:34px;width:24px;height:24px;border-radius:50%"></div>
    <div class="silhouette" role="img" aria-label="Standing dog silhouette" style="left:82px;top:336px;width:56px;height:46px;border-radius:8px"></div>
    <div class="silhouette" role="img" aria-label="Sitting cat silhouette" style="left:257px;top:318px;width:30px;height:60px;border-radius:14px"></div>

    <div class="panel about">
      <p class="tiny">Hollowmere Pet Lodge &amp; Spa is a high-quality, full-service pet facility with pet-owning and pet-loving caregivers who will treat your pets like family, giving them the expert care and attention they require and deserve. We are passionate about animals and understand that they all have their own individual personalities and quirks. We take the time to get to know your dog or cat and give him or her the individual care your pet needs. We specialize in providing everything for the well-loved pet, including dog daycare, dog and cat boarding, dog and cat grooming, and a unique selection of merchandise retail.</p>
      <h3 class="heading">Grooming</h3>
      <p class="tiny">At Hollowmere Pet Lodge &amp; Spa our experienced grooming staff will take the time to make your pet look fabulous using state-of-the-art grooming equipment and techniques. Our professional groomers are friendly pet lovers who take great pride in their work. Whether you need professional grooming, premium bathing services, or breed standard cuts, our staff will ensure your pet walks away from our spa looking his or her best! Grooming and styling are individual spa services and prices will vary depending upon the breed, size, style, condition and temperament of the pet. Hollowmere Pet Lodge &amp; Spa Groomers are eager to provide a thorough consultation free of charge upon arrival. At this time please express your requests, concerns, and any price questions to your stylist.</p>
      <div class="photo" role="img" aria-label="Photo of groomers with dogs in the salon"></div>
    </div>

    <div class="panel rates">
      <h3 class="heading">Daycare</h3>
      <p class="tiny">Our dog daycare play rooms are supervised by our trained staff members so that your pet can have a safe place to socialize, exercise, and expend excess energy. We have dedicated playrooms to accommodate different sized guests with different temperaments. We provide your pet with a safe, clean and fun environment that will remind your best friend of home.</p>
      <h3 class="heading">Pricing and Requirements for Daycare and Boarding</h3>
      <p class="tiny">We require all guests to complete an evaluation prior to entering our daycare program. This evaluation will determine whether your pet is safe to play with other dogs and members of our staff.</p>
      <h3 class="heading">For All Canine Guests:</h3>
      <p class="tiny">•Proof of current DHPP (yearly), Rabies, and Bordetella (yearly).<br>•All vaccinations must be current before lodging/daycare.</p>
      <h3 class="heading">For All Feline Guests</h3>
      <p class="tiny">•Proof of current Rabies, and FVRCP Vaccinations.<br>•All vaccinations must be current before lodging.</p>
      <table class="rate-table">
        <tr><td>Daycare Pricing</td><td>Single Pet</td><td>Add'l Pet</td><td>3rd Pet</td></tr>
        <tr><td>4 Hours</td><td>$12</td><td>$9</td><td>$8</td></tr>
        <tr><td>6 Hours</td><td>$17</td><td>$15</td><td>$10</td></tr>
        <tr><td>Full Day</td><td>$22</td><td>$18</td><td>$12</td></tr>
        <tr><td>Dog Boarding</td><td>$34</td><td>$26</td><td>$21</td></tr>
        <tr><td></td><td></td><td></td><td></td></tr>
        <tr><td>Cat Boarding</td><td>$19</td><td>$15</td><td></td></tr>
      </table>
      <div class="photo" role="img" aria-label="Photo of the Pim and Tessel style boutique wall with leads and accessories"></div>
    </div>

    <div class="panel stay tiny">
      <h3 class="heading">While Your Dog is With Us...</h3>
      <p>-Brand new state of the art suite systems for boarding</p>
      <p>-supervised off leash dog daycare</p>
      <p>- We offer 24/7 supervision to ensure a safe, relaxing and comfortable experience with 12 webcams for added security</p>
      <p>-Pet Boutique with toys, treats, beds, clothes, collars &amp; leashes</p>
      <p>-Committed and trained staff to provide the best care</p>
      <p>-equipped with central heat and air conditioning throughout</p>
      <p>-Elevated beds</p>
      <p>-A secure, fenced-in facility</p>
      <p>-Wellness checks provided and continuous monitoring of your dog throughout the day</p>
      <p>-Opportunities to play and socialize with other dog boarding and dog daycare guests SAFELY, under trained staff supervision</p>
      <h3 class="heading">While Your Cat is With Us...</h3>
      <p style="margin:0">-brand new state of the art kitty condo modular units<br>-comfortable bedding for each guest<br>-every guest will have playtimes individually<br>-Your pet will thoroughly enjoy the privacy in their luxurious boarding room away from our canine guests</p>
      <div class="photo" role="img" aria-label="Photo of a linen pet bed bag"></div>
    </div>
  </section>

</main>
</body>
</html>
```